Business Card Design Project - bel soravin group

dear Sirs

we need business card design for our group ( BEL Soravin Group ) , i have got the Logo design of our group from pixel harbor in previous , so all need details relating to our group i think available with you, as well as the the chosen logo design

we hope to provide us with business card logo that to be appropaite and satisfactory to us .

thanks

note : logo design of our group is attached .
Updates

Reason: please extend the deadline of my project for additional 15 days because i didn't received appropriate design for our gruop yet . kindly beaware that i have received 77 design till now , supossed to send me 200-250 design at least . thanks

Target Market(s)

contents
-

name : Korvan EL Mistrani

position : Operation Manager

Industry/Entity Type

Business

Requirements
Must have

• person name

group logo
Nice to have
• logo color matching with back background

```html
<!DOCTYPE html>
<html lang="en">
<head>
<meta charset="UTF-8">
<title>BEL Soravin Group – Business Card</title>
<link rel="stylesheet" href="https://fonts.googleapis.com/css2?family=Source+Sans+3:wght@400;600&display=swap">
<style>
  :root {
    --page-bg: #ffffff;
    --front-bg: #f7f6ee;
    --back-bg: #ebdcb0;
    --brand-blue: #2f5d93;
    --name-blue: #3d6a98;
    --text-blue: #4a82bd;
  }
  html, body {
    margin: 0;
    padding: 0;
    width: 1200px;
    height: 333px;
    overflow: hidden;
    background: var(--page-bg);
  }
  .sheet {
    position: relative;
    width: 1200px;
    height: 333px;
    font-family: "Source Sans 3", sans-serif;
  }
  .card {
    position: absolute;
    top: 0;
    height: 333px;
  }
  .card--front {
    left: 0;
    width: 583px;
    background: var(--front-bg);
  }
  .card--back {
    left: 618px;
    width: 582px;
    background: var(--back-bg);
  }
  .brand {
    position: absolute;
    left: 12px;
    top: 10px;
    display: flex;
    align-items: center;
    gap: 8px;
    color: var(--brand-blue);
    font-size: 25px;
    font-weight: 400;
    letter-spacing: 0.5px;
    line-height: 1;
  }
  .brand__mark {
    width: 14px;
    height: 14px;
    background: var(--brand-blue);
  }
  .person {
    position: absolute;
    left: 374px;
    top: 80px;
  }
  .person__name {
    margin: 0;
    color: var(--name-blue);
    font-size: 25px;
    font-weight: 400;
    line-height: 1.1;
  }
  .person__role {
    margin: 4px 0 0 1px;
    color: var(--text-blue);
    font-size: 15px;
    font-weight: 400;
    line-height: 1.2;
  }
  .contacts {
    position: absolute;
    left: 8px;
    top: 184px;
    margin: 0;
    padding: 0;
    list-style: none;
    color: var(--text-blue);
    font-size: 14.5px;
    line-height: 22.7px;
  }
</style>
</head>
<body>
  <main class="sheet">
    <section class="card card--front" aria-label="Business card front">
      <div class="brand">
        <span class="brand__mark" aria-hidden="true"></span>
        <span class="brand__name">BEL Soravin Group</span>
      </div>
      <div class="person">
        <h1 class="person__name">Korvan EL Mistrani</h1>
        <p class="person__role">Operation Manager</p>
      </div>
      <ul class="contacts">
        <li>Tel :</li>
        <li>Fax :</li>
        <li>Mobile :</li>
        <li>Email address :</li>
        <li>Web site :</li>
        <li>PO. Box :</li>
      </ul>
    </section>
    <section class="card card--back" aria-label="Business card back"></section>
  </main>
</body>
</html>
```